Re jig a A4 Instructional Flyer

We need an established A4 instructional Flyer (2 pages x A4) - to be rejigged in Harcourt College of Learning Branding to look fresh and new.

Permissions have been received to rejig this Medical Triage Chart. Fresh branding and setting out (fonts) required.

FOOTER NOTES : to be inserted at the bottom of the A4 instruction sheet

Harcourt College produced with permissions from Outback Care Alliance, produced by Outback Care Alliance with Clinic Circle Uptown with permissions from Southern Lakes Carewell Hub. Harcourt acknowledges the NBFPS Standards Criterion 3.2.3 Practice Training and Education in Triage

Target Market(s)

Medical Practices

Industry/Entity Type

Health

Font styles to use
Serif

Colors
0255a3
f78f20

Requirements
Must have
• Professional
• Pops of colour in the chart.
• This chart is to be USED and is VISUAL (no boring grey words throughout)
• PROBS SANS SERIF but SERIF for titles OK
Nice to have
• look at www.harcourtlearn.edu.au FOR BRANDING look and feel

```html
<!DOCTYPE html>
<html lang="en">
<head>
<meta charset="utf-8">
<title>Triage: A guide to urgency for non-clinical staff</title>
<link rel="stylesheet" href="https://fonts.googleapis.com/css2?family=Arimo:wght@400;700&family=Mulish:wght@600;700&family=Roboto+Condensed:wght@400;500&family=Libre+Baskerville:wght@400;700&display=swap">
<style>
:root{
  --brand-blue:#0255a3;
  --brand-orange:#f78f20;
  --navy:#0b3a6e;
  --red:#e3141b;
  --pink:#e5176f;
  --ink:#1a1a1a;
  --panel:rgba(240,243,248,.86);
  --cat1:#e3141b;
  --cat2:#f78f20;
  --cat3:#ee7d9b;
  --cat4:#11a3a3;
  --cat5:#0255a3;
  --cat6:#8dc21f;
}
*{box-sizing:border-box;margin:0;padding:0}
html,body{width:1200px;height:1200px;overflow:hidden;background:#fff}
body{position:relative;font-family:Arimo,Arial,sans-serif;color:var(--ink)}
.page{position:absolute;left:186px;width:828px;height:585px;overflow:hidden}
.page--guide{top:5px}
.page--scenarios{top:611px}
.photo{position:absolute;inset:0}
.page--guide .photo{background:linear-gradient(180deg,#e9c2a0 0%,#dcb596 22%,#6f9fcb 32%,#86b0d6 55%,#c7a0b6 78%,#dba88e 100%)}
.page--scenarios .photo{background:linear-gradient(180deg,#d8b49a 0%,#b9a7b7 15%,#8c8fb6 45%,#a99ab9 70%,#d6a98e 100%)}
.frame{position:absolute;left:14px;top:14px;right:14px;bottom:14px;border:1.5px solid rgba(255,255,255,.9);pointer-events:none}

/* header */
.college-badge{position:absolute;left:41px;top:25px;width:108px;height:108px;border-radius:50%;background:#fff;border:3px solid var(--brand-orange);display:flex;align-items:center;justify-content:center;text-align:center;font-family:Mulish,sans-serif;font-weight:700;font-size:11px;line-height:1.3;color:var(--brand-blue);padding:14px}
.guide-title{position:absolute;left:160px;top:38px;font-family:Mulish,sans-serif;font-weight:700;font-size:24px;line-height:32px;color:#fff}
.tool-brand{position:absolute;left:562px;top:15px;width:252px;height:52px;background:#e9e9e9;padding:10px 14px 0 80px}
.tool-brand .name{font-family:Arimo,sans-serif;font-weight:700;font-size:19px;color:var(--brand-blue)}
.tool-brand .tag{font-size:7px;color:#444;margin-top:2px}
.tool-tag{position:absolute;left:688px;top:71px;width:126px;height:22px;background:var(--pink);color:#fff;font-size:17px;text-align:right;padding:1px 6px 0 0}

/* flow */
.box{position:absolute;background:#fff;border:1px solid #888;font-size:9.5px;line-height:1.2}
.box--q{font-weight:700;display:flex;align-items:center;justify-content:center;text-align:center}
.box--yes{border:1.5px solid var(--brand-blue);color:var(--brand-blue)}
.box--no{border:1.5px solid var(--brand-orange);color:#c0620a}
.box--record{padding:3px 6px;border-top:3px solid var(--brand-blue)}
.box--record h4{font-size:9.5px;text-align:center;margin-bottom:2px;color:var(--brand-blue)}
ul.dots{list-style:none}
ul.dots li{position:relative;padding-left:11px}
ul.dots li::before{content:"";position:absolute;left:2px;top:.45em;width:3.5px;height:3.5px;border-radius:50%;background:currentColor}
.box--emerg{padding:4px 7px;font-size:9.3px;border-top:3px solid var(--red)}
.emerg-title{color:var(--red);font-weight:700;text-align:center}
.emerg-call{color:var(--red);font-weight:700;text-align:center}
.flow-arrows{position:absolute;left:0;top:0}

/* table */
.triage-table{position:absolute;left:42px;top:273px;width:742px;border-collapse:collapse;table-layout:fixed;font-size:9.2px;line-height:1.17}
.triage-table th{background:var(--brand-blue);color:#fff;font-size:6.8px;letter-spacing:.4px;height:14px;font-weight:700;border:1px solid #7f9cbf;border-bottom-width:3px}
.triage-table th:nth-child(1){background:var(--navy);border-bottom-color:var(--navy)}
.triage-table th:nth-child(2){border-bottom-color:var(--cat1)}
.triage-table th:nth-child(3){border-bottom-color:var(--cat2)}
.triage-table th:nth-child(4){border-bottom-color:var(--cat3)}
.triage-table th:nth-child(5){border-bottom-color:var(--cat4)}
.triage-table th:nth-child(6){border-bottom-color:#5fa8ee}
.triage-table th:nth-child(7){border-bottom-color:var(--cat6)}
.triage-table td{border:1px solid #7e8ea0;background:rgba(236,241,248,.85);vertical-align:top;padding:2px 3px}
.triage-table .instr{padding:3px 4px;color:var(--navy)}
.triage-table tr.body td{height:144px}
.triage-table tr.tell td{height:37px;vertical-align:middle}
.triage-table tr.act td{height:25px;vertical-align:middle}
.triage-table tr.tell td:not(.instr),.triage-table tr.act td:not(.instr){text-align:center;font-weight:700}
.triage-table tr.file td:not(.instr){font-weight:400}
.triage-table tr.tell td:nth-child(2){color:var(--cat1)}
.triage-table tr.tell td:nth-child(3){color:#d9720c}
.triage-table tr.tell td:nth-child(4){color:#d4466c}
.triage-table tr.tell td:nth-child(5){color:#0b8787}
.triage-table tr.tell td:nth-child(6){color:var(--cat5)}
.triage-table tr.tell td:nth-child(7){color:#5f8f0e}
.triage-table tr.body td:nth-child(2) li::before{background:var(--cat1)}
.triage-table tr.body td:nth-child(3) li::before{background:var(--cat2)}
.triage-table tr.body td:nth-child(4) li::before{background:var(--cat3)}
.triage-table tr.body td:nth-child(5) li::before{background:var(--cat4)}
.triage-table tr.body td:nth-child(6) li::before{background:var(--cat5)}
.triage-table tr.body td:nth-child(7) li::before{background:var(--cat6)}
.site-url{position:absolute;left:564px;top:538px;color:#fff;font-size:17px;letter-spacing:.3px}

/* page 2 */
.band{position:absolute;left:0;top:14px;width:828px;height:47px;background:rgba(232,205,180,.55)}
.fdt-title{position:absolute;left:58px;top:29px;font-size:17px;font-weight:400;color:#222}
.fdt-title b{color:var(--brand-orange);font-weight:700;margin-right:20px}
.col{position:absolute;top:65px;background:var(--panel);padding:10px 8px 0 8px;font-size:8.8px;line-height:1.22;border-top:3px solid var(--brand-blue)}
.col h3{font-family:"Roboto Condensed",sans-serif;font-weight:500;font-size:12.5px;text-transform:uppercase;margin:2px 0 5px;color:var(--brand-blue)}
.col ul.dots li{margin-bottom:6px;padding-left:16px}
.col ul.dots li::before{background:var(--brand-orange)}
.col ol{list-style:none;counter-reset:n}
.col ol li{counter-increment:n;position:relative;padding-left:16px;margin-bottom:6px}
.col ol li::before{content:counter(n)".";position:absolute;left:0;font-weight:700;color:var(--brand-orange)}
.c1{color:var(--cat1);font-weight:700}.c2{color:#e07a0e;font-weight:700}.c3{color:#e0608a;font-weight:700}.c4{color:var(--cat4);font-weight:700}.c5{color:var(--cat5);font-weight:700}.c6{color:#74a812;font-weight:700}
.red{color:var(--red);font-weight:700}
.note{font-style:italic;font-weight:700;color:var(--navy);margin-top:6px}
.emerg-panel{position:absolute;left:56px;top:393px;width:236px;height:108px;background:rgba(236,231,242,.9);border-top:3px solid var(--red);padding:5px 6px;font-size:8.8px;line-height:1.2}
.emerg-panel ul.dots li{margin-bottom:1px}
.credits{position:absolute;left:0;top:509px;width:828px;height:56px;background:rgba(214,150,100,.82);border-top:3px solid var(--brand-orange);color:#fff;font-family:"Libre Baskerville",serif;font-size:11.6px;line-height:16px;text-align:center;padding-top:2px}
</style>
</head>
<body>

<section class="page page--guide" aria-label="Triage guide">
  <div class="photo" role="img" aria-label="Soft background photograph of a hand reaching towards a touch screen"></div>
  <div class="frame"></div>

  <div class="college-badge">Harcourt College of Learning</div>
  <h1 class="guide-title">Triage: A guide to urgency for<br>non-clinical staff in general practice<br>for telephone and walk in presentations</h1>
  <div class="tool-brand"><div class="name">Care Compass</div><div class="tag">Strengthening general practice in WA</div></div>
  <div class="tool-tag">Tool</div>

  <div class="box box--q" style="left:42px;top:149px;width:170px;height:22px">Do you have an urgent problem?</div>
  <div class="box box--q box--yes" style="left:239px;top:149px;width:39px;height:24px">YES</div>
  <div class="box box--q" style="left:72px;top:188px;width:100px;height:26px">NO / I DON'T KNOW</div>
  <div class="box box--q" style="left:42px;top:230px;width:170px;height:31px;font-weight:400">The next available appointment is . . .<br>Is this ok?</div>
  <div class="box box--q box--no" style="left:239px;top:232px;width:38px;height:23px">NO</div>
  <div class="box box--record" style="left:310px;top:151px;width:228px;height:104px">
    <h4>Record the patient's phone number</h4>
    <ul class="dots">
      <li>What is the name and age of the patient?</li>
      <li>What is the nature of the problem?</li>
      <li>What is the duration of the problem?</li>
      <li>What is the severity of the problem?</li>
      <li>Has the patient had any previous major health problems?</li>
      <li>Select a category below and follow instructions.</li>
    </ul>
  </div>
  <div class="box box--emerg" style="left:544px;top:151px;width:240px;height:104px">
    <div class="emerg-title">EMERGENCY ACTION PLAN</div>
    <ul class="dots">
      <li>Remain calm and do not panic.</li>
      <li>Be aware and respond to the needs of the emergency.</li>
      <li>Assess which patient needs to take priority.</li>
      <li>Deal with any injury or illness in order of severity.</li>
    </ul>
    <div class="emerg-call">CALL 000<br>FOR AMBULANCE, POLICE OR FIRE</div>
  </div>

  <svg class="flow-arrows" width="828" height="300" viewBox="0 0 828 300" aria-hidden="true">
    <defs><marker id="ah" viewBox="0 0 6 6" refX="5" refY="3" markerWidth="5" markerHeight="5" orient="auto"><path d="M0,0L6,3L0,6z" fill="#f78f20"/></marker></defs>
    <g stroke="#f78f20" stroke-width="1.6" fill="none" marker-end="url(#ah)">
      <line x1="213" y1="160" x2="237" y2="160"/>
      <line x1="279" y1="160" x2="308" y2="160"/>
      <line x1="122" y1="172" x2="122" y2="186"/>
      <line x1="122" y1="215" x2="122" y2="228"/>
      <line x1="213" y1="243" x2="237" y2="243"/>
      <line x1="278" y1="243" x2="308" y2="243"/>
    </g>
  </svg>

  <table class="triage-table">
    <colgroup><col style="width:65px"><col><col><col><col><col><col></colgroup>
    <tr><th>INSTRUCTION</th><th>CATEGORY 1</th><th>CATEGORY 2</th><th>CATEGORY 3</th><th>CATEGORY 4</th><th>CATEGORY 5</th><th>CATEGORY 6</th></tr>
    <tr class="body">
      <td class="instr">Practice to ask the patient or caller to describe the problem/s, and categorise accordingly:</td>
      <td><ul class="dots"><li>Chest pain</li><li>Breathing difficulties/ trouble talking</li><li>Facial swelling and rash</li><li>Collapse/altered consciousness</li><li>Facial/limb weakness</li><li>Extensive burns</li><li>Sick patient you have concerns about</li></ul></td>
      <td><ul class="dots"><li>Fitting</li><li>Bleeding (heavy or persistent)</li><li>Spinal or head injury/ trauma</li><li>Snake bite</li><li>Heart palpitations</li><li>In labour/ruptured membranes</li><li>Neck stiffness/altered consciousness</li></ul></td>
      <td><ul class="dots"><li>Unable to urinate</li><li>Unwell 'floppy' infant</li><li>Poisoning/overdose</li><li>Eye injuries/chemical in the eye</li><li>Pain (severe)</li><li>Injured limb/possible fracture</li></ul></td>
      <td><ul class="dots"><li>Unwell child/elder with fever, vomiting, diarrhoea or pain for &gt;24 hours</li><li>Pregnancy: pain or bleeding; reduced foetal movement</li><li>Abuse or assault</li><li>Visual disturbance</li><li>Patient or carer with extreme concern</li><li>Psychological distress</li></ul></td>
      <td><ul class="dots"><li>Unwell child/elderly with fever, vomiting, diarrhoea or pain for &lt;24 hours</li><li>Rash (severe)</li><li>Cut/laceration</li><li>Severe flu like symptoms</li></ul></td>
      <td><ul class="dots"><li>Adult with fever, but otherwise well</li><li>Post op problems</li><li>Eye or ear infections/pain</li><li>Adult with continuous vomiting and/or diarrhoea for &gt;24 hrs</li></ul></td>
    </tr>
    <tr class="tell">
      <td class="instr">Tell the caller to:</td>
      <td>Call 000</td><td>Go to emergency department now</td><td>Put call through to nurse/doctor</td><td>Come to surgery now Advise the on-call nurse/doctor</td><td>Come to surgery today and call back if gets worse</td><td>Make an appointment within 24 hours and call back if gets worse</td>
    </tr>
    <tr class="act">
      <td class="instr">Practice/ Receptionist</td>
      <td>Call nurse/doctor for help immediately</td><td>Interrupt nurse/doctor immediately</td><td>Advise nurse/doctor now</td><td>Discuss with nurse/doctor</td><td>Inform nurse/doctor within 30 minutes</td><td>Inform nurse/doctor</td>
    </tr>
    <tr class="act file">
      <td class="instr">Practice/ Receptionist</td>
      <td>Retrieve patient file Document activity</td><td>Retrieve patient file Document activity</td><td>Retrieve patient file Document activity</td><td>Retrieve patient file Document activity</td><td>Retrieve patient file Document activity</td><td>Retrieve patient file Document activity</td>
    </tr>
  </table>

  <div class="site-url">www.harcourtlearn.edu.au</div>
</section>

<section class="page page--scenarios" aria-label="Front desk triage">
  <div class="photo" role="img" aria-label="Soft background photograph of staff walking through a clinic corridor"></div>
  <div class="band"></div>
  <div class="frame"></div>
  <h2 class="fdt-title"><b>FRONT DESK TRIAGE</b>How to manage common scenarios faced by reception staff</h2>

  <div class="col" style="left:54px;width:238px;height:326px">
    <h3>Is this an emergency?</h3>
    <ul class="dots">
      <li>When answering the telephone, all callers should be asked if the matter is an emergency prior to being placed on hold: Ask the patient, <i>“Is this an emergency or can I place you on hold for a moment?”</i></li>
      <li>Consider the TRIAGE STEPS and CATEGORIES listed on the reverse of this document to assess the patient's status.</li>
    </ul>
    <h3>Ask the patient – Triage steps</h3>
    <ol>
      <li>Confirm the patient's name and phone number.</li>
      <li>Does the patient attend the surgery? (ie Does the practice have previous medical records to hand?)</li>
      <li>Location. (<i>“Are you at home?” “Are you alone?”</i>)</li>
      <li>Nature of their problem. (Patient may prefer to speak to the practice nurse or on call doctor.)</li>
      <li>Duration of their symptoms. (<i>“How long have you felt like this?”</i>)</li>
      <li>Severity of their problem. (<i>“On a scale of 1 to 10 how severe is the pain?”</i> [if applicable].)</li>
      <li>Any previous major health problems. (<i>“Are you on any medication?” “Do you have any allergies?”</i>)</li>
    </ol>
  </div>
  <div class="emerg-panel">
    <div class="emerg-title">EMERGENCY ACTION PLAN</div>
    <ul class="dots">
      <li>Remain calm and don not panic.</li>
      <li>Be aware and respond to the needs of the emergency.</li>
      <li>Assess which patient needs to take priority.</li>
      <li>Deal with any injury or illness in order of severity.</li>
    </ul>
    <div class="emerg-call">CALL 000<br>FOR AMBULANCE, POLICE OR FIRE</div>
  </div>

  <div class="col" style="left:300px;width:238px;height:436px">
    <h3>On the day emergencies in the clinic</h3>
    <ul class="dots">
      <li><span class="c1">Category 1</span> patients should immediately be seen by the on-call doctor or other medical professional on duty.</li>
      <li><span class="c2">Category 2</span> patients should be directed to the emergency department of their nearest hospital.</li>
      <li><span class="c3">Category 3</span> patients or patients with worsening symptoms should be referred to the practice nurse or on call doctor.</li>
      <li><span class="c4">Category 4</span> patients should be advised to attend the clinic immediately and triaged by the practice nurse (may then be slotted in between appointments or at the end of the session).</li>
      <li><span class="c5">Category 5</span> patients should make an appointment for the day and be advised to call back if symptoms worsen.</li>
      <li><span class="c6">Category 6</span> patients should make an appointment within 24 hours and call back if symptoms worsen.</li>
    </ul>
    <h3>Patients presenting with symptoms of potential communicable diseases</h3>
    <ul class="dots">
      <li>Such as ‘influenza’(‘flu), measles, chicken pox should be isolated to a secluded area of the medical practice such as the nurses' office. Where possible, a notice of isolation is to be fixed to the door to limit access in this area.</li>
      <li>Patients with ‘flu like symptoms should be required to wear a surgical mask.</li>
      <li>If the patient is bleeding or vomiting, put gloves on before you assist them.</li>
    </ul>
  </div>

  <div class="col" style="left:544px;width:236px;height:436px">
    <h3>Scheduling care</h3>
    <ul class="dots">
      <li>Reception staff should reserve several unbooked appointment times each day for ‘on the day’ urgent appointments such as unwell children and the elderly, lacerations and suspected fractures.</li>
      <li>If your practice does not operate on an appointment system, patients should be triaged on walk in and advised of the expected waiting time to see the doctor, nurse or Aboriginal health worker.</li>
      <li>Where a patient is assessed as in need of urgent medical attention over the telephone, advise the caller to hang up and call <span class="red">000</span> immediately for an ambulance.</li>
      <li>Where a receptionist is unable to determine the urgency of a telephone call, the patient should be transferred to the practice nurse or on-call doctor for triage.</li>
      <li>If a patient presents in person and requires urgent medical assistance after the doctor has left – call <span class="red">000</span> for ambulance.</li>
      <li>Clinical staff treating the patient should wear as a minimum, a surgical mask, gloves and when collecting nose and/or throat swabs, protective eyewear.</li>
    </ul>
    <p class="note">All emergency cases dealt with by reception should be recorded by the staff member involved in the patient health record in addition to the clinical notes recorded by the practice nurse or doctor/s treating the patient.</p>
  </div>

  <div class="credits">Harcourt College produced with permissions from Outback Care Alliance,<br>produced by Outback Care Alliance with Clinic Circle Uptown with permissions from Southern Lakes Carewell Hub.<br>Harcourt acknowledges the NBFPS Standards Criterion 3.2.3 Practice Training and Education in Triage</div>
</section>

</body>
</html>
```